Bright Oak Family Dentistry
Logo For Dental Office - Medical
Logo For Dental Office
Professional
Mira Tolvanen
DMD
2687 Pemberly Lane Suite 214 Virginia Beach, VA 23461
brightoak482@mailnest.com
brightoakfamilydentistry.com
I would like shades of blue in my logo
Appointment card on the back
kivo-darrel kivo-darrel
Can you give me an existing copy of your logo.
lumengrit lumengrit
Hello sir, Can you please provide your logo? :)

```html
<!DOCTYPE html>
<html lang="en">
<head>
<meta charset="utf-8">
<title>Bright Oak Family Dentistry – Business Card</title>
<link href="https://fonts.googleapis.com/css2?family=Arimo:wght@400&family=Tinos:wght@400&display=swap" rel="stylesheet">
<style>
  :root {
    --page-bg: #ffffff;
    --card-bg: #ffffff;
    --card-edge: #d9dadc;
    --brand-blue: #1b8fcf;
    --name-blue: #2a93c9;
    --body-grey: #4f5256;
    --band-dark: #8e9094;
    --band-light: #d4d5d7;
  }
  html, body {
    margin: 0;
    padding: 0;
    width: 1200px;
    height: 756px;
    overflow: hidden;
    background: var(--page-bg);
  }
  .business-card {
    position: absolute;
    left: 50px;
    top: 101px;
    width: 1100px;
    height: 553px;
    background: var(--card-bg);
    border: 2px solid var(--card-edge);
    border-radius: 30px;
    box-sizing: border-box;
    overflow: hidden;
    font-family: "Arimo", Arial, sans-serif;
  }
  .brand-mark {
    position: absolute;
    left: 85px;
    top: 190px;
    color: var(--brand-blue);
    font-family: "Arimo", Arial, sans-serif;
    font-weight: 400;
  }
  .brand-mark .brand-dot {
    position: absolute;
    left: 0;
    top: 8px;
    width: 30px;
    height: 30px;
    border-radius: 50%;
    background: var(--brand-blue);
  }
  .brand-mark .brand-name {
    margin: 0 0 0 44px;
    font-size: 50px;
    line-height: 1;
    letter-spacing: 1px;
    white-space: nowrap;
  }
  .brand-mark .brand-tagline {
    margin: 10px 0 0 100px;
    font-size: 38px;
    line-height: 1;
    white-space: nowrap;
  }
  .divider {
    position: absolute;
    left: 512px;
    top: 100px;
    width: 4px;
    height: 323px;
    background: var(--brand-blue);
  }
  .person-name {
    position: absolute;
    left: 567px;
    top: 92px;
    margin: 0;
    font-family: "Tinos", "Times New Roman", serif;
    font-weight: 400;
    font-size: 56px;
    line-height: 1;
    color: var(--name-blue);
    white-space: nowrap;
  }
  .person-title {
    position: absolute;
    left: 815px;
    top: 150px;
    margin: 0;
    font-family: "Tinos", "Times New Roman", serif;
    font-size: 28px;
    line-height: 1;
    color: var(--name-blue);
  }
  .address {
    position: absolute;
    left: 567px;
    top: 302px;
    margin: 0;
    font-style: normal;
    font-size: 29px;
    line-height: 40px;
    color: var(--body-grey);
    white-space: nowrap;
  }
  .contact {
    position: absolute;
    left: 567px;
    top: 437px;
    margin: 0;
    font-size: 26px;
    line-height: 35px;
    color: var(--body-grey);
    white-space: nowrap;
  }
  .footer-band {
    position: absolute;
    left: 0;
    bottom: 0;
    width: 100%;
    height: 48px;
    background: linear-gradient(90deg, var(--band-dark) 0%, var(--band-light) 50%, var(--band-dark) 100%);
  }
</style>
</head>
<body>
  <div class="business-card">
    <div class="brand-mark" aria-label="Bright Oak Family Dentistry">
      <span class="brand-dot"></span>
      <p class="brand-name">BRIGHT OAK</p>
      <p class="brand-tagline">Family Dentistry</p>
    </div>

    <div class="divider"></div>

    <h1 class="person-name">Mira Tolvanen</h1>
    <p class="person-title">DMD</p>

    <address class="address">
      2687 Pemberly Lane<br>
      Suite 214,Virginia Beach,<br>
      VA 23461, Ph: 757-555-0148
    </address>

    <p class="contact">
      Email: brightoak482@mailnest.com<br>
      www.brightoakfamilydentistry.com
    </p>

    <div class="footer-band"></div>
  </div>
</body>
</html>
```